Indonesian B2B Company (Varo Ingredients) - Stationery Design

Varo Ingredients needs a corporate, bold and professional-looking stationery design.

Varo Ingredients is a new Indonesian company manufacturing, marketing and distributing various ingredients / raw materials such as flavours, fragrance, colours, sweeteners, preservatives for the food & beverage, pharmaceutical, personal care and other household goods industries.

It is a business to business (B2B) company as we supply various natural and synthetic raw materials to various consumer goods manufacturers. We therefore need a logo/identity with corporate and industrial style.

Varo Ingredients is a startup company which belongs to a larger Varo Tunggal group of companies (http://varotunggal.dealpathway.com/about) that focuses in the mining, petroleum and energy businesses. Varo Ingredients would like to focus in providing good quality, safe, reliable and affordable ingredients for the industries. Our tagline is "Ingredients for Your Success"
Updates

We have updated some information including our requirements and contact details to be shown in the stationery. Please check the project brief.

Regards,

Varo Ingredients

Target Market(s)

Manufacturers of food & beverages, personal care, pharmaceutical and other FMCG factories.

Industry/Entity Type

Business

Requirements
Must have
• Smart, professional and corporate touches in the stationery designs. We require designs for:
1. Letterhead
2. Envelope (with and without window)
3. Name card
4. Powerpoint presentation template
5. CD label
6. Small memo / with compliments card

Contact details:

Company name:
PT Varo Ingredients

Address:
Ruko Melati Sentosa Utara, Blok K07 no: 15-16
Duren Sawit Selatan, 13470
Indonesia

Tel:+62 21 738 2906
Fax:+62 21 738 2907
Email: info@varo-ingredients.co.id
Website: www.varo-ingredients.co.id

```html
<!DOCTYPE html>
<html lang="en">
<head>
<meta charset="utf-8">
<title>Varo Ingredients – Presentation Template</title>
<link rel="stylesheet" href="https://fonts.googleapis.com/css2?family=Source+Sans+3:wght@400;600&display=swap">
<style>
  :root {
    --brand-red: #c1272d;
    --brand-red-light: #e8504c;
    --ink: #55575b;
    --paper-centre: #ffffff;
    --paper-edge: #e4e5e7;
    --on-red: #ffffff;
  }
  * { margin: 0; padding: 0; box-sizing: border-box; }
  html, body { width: 1200px; height: 900px; overflow: hidden; }
  body { font-family: "Source Sans 3", sans-serif; }

  .slide {
    position: relative;
    width: 1200px;
    height: 900px;
    overflow: hidden;
    background: radial-gradient(ellipse at 48% 50%, var(--paper-centre) 0%, #f3f3f4 45%, var(--paper-edge) 100%);
  }
  .slide-shapes { position: absolute; inset: 0; }

  .brand {
    position: absolute;
    left: 55px;
    top: 100px;
    display: flex;
    align-items: center;
    gap: 10px;
  }
  .brand-square {
    width: 16px;
    height: 16px;
    background: var(--brand-red);
  }
  .brand-name {
    font-size: 25px;
    font-weight: 400;
    color: var(--ink);
    line-height: 1;
  }

  .contact, .address {
    position: absolute;
    font-style: normal;
    color: var(--on-red);
    font-size: 9.6px;
    line-height: 12.2px;
    font-weight: 600;
    white-space: nowrap;
  }
  .contact { left: 872px; top: 7px; }
  .address { left: 991px; top: 80px; }

  .footer-web {
    position: absolute;
    left: 0;
    right: 0;
    bottom: 4px;
    text-align: center;
    color: var(--on-red);
    font-size: 36px;
    font-weight: 400;
    line-height: 1.2;
  }
</style>
</head>
<body>
<main class="slide">
  <svg class="slide-shapes" viewBox="0 0 1200 900" width="1200" height="900" aria-hidden="true">
    <path class="header-band" fill="var(--brand-red)"
      d="M0,150 C400,195 900,180 1200,132 L1200,0 L980,0 C960,90 700,150 0,150 Z"/>
    <path class="header-accent" fill="var(--brand-red-light)"
      d="M300,154 C700,150 840,90 860,0 L980,0 C960,90 700,150 300,154 Z"/>
    <path class="footer-band" fill="var(--brand-red)"
      d="M0,900 L0,880 Q600,815 1200,870 L1200,900 Z"/>
  </svg>

  <header class="brand">
    <span class="brand-square"></span>
    <span class="brand-name">Varo Ingredients</span>
  </header>

  <address class="contact">
    Tel:+62 21 738 2906<br>
    Fax:+62 21 738 2907<br>
    Email: info@varo-ingredients.co.id<br>
    Website: www.varo-ingredients.co.id
  </address>

  <address class="address">
    PT Varo Ingredients<br>
    Ruko Melati Sentosa Utara, Blok K07 no: 15-16<br>
    Duren Sawit Selatan, 13470<br>
    Indonesia
  </address>

  <footer class="footer-web">www.varo-ingredients.co.id</footer>
</main>
</body>
</html>
```